Visit card for Luxury Alpine home

Velvet Ridge Chalet (Hinterthal, Austria) – visit card

Brief: To design a visit card (4/4) that can be both left for existing guests and handed out to friends/business contacts to promote our luxury holiday home in the Austrian alps which can be rented year -round but primarily for summer (hiking/biking/golf) and winter (skiing). Primary focus is for family as its a 3br/3ba place that is usually booked for either a larger family or two families.

Basic information required/purpose: email/contact info. Basic information about the place, location, possibly some ideas/icons about what to do. Imagery that gives people the idea about luxury/fun/mountains etc. Hopefully the card would be something to interest them enough to check out the website and eventually make a direct booking with us.

Our details and photos:

https://velvetridgechalet.com
https://www.facebook.com/velvetridgechalet/

contact information for people to book:
stay.brenvale@larkpost.net
+420 604918352

some other resources:

http://www.tamrisberg-info.at/en/vacation.html
the moutains are called Hochkoenig and our village is Hinterthal which is next to Maria alm

Target Market(s)

European (winter) and Middle-Eastern (summer) families.

Industry/Entity Type

Travel

Contact Information for Business Card

standard 4/4 to be used for prospect

Font styles to use
Sans Serif

Colors

Designer to choose colors to be used in the design.

Requirements
Must have
• all relevant information for the client to contact us
• colorful/luxury imagery of the property (we can provide better photo quality that the web downloads)
Nice to have
• not particular about fonts. preferring subdued colours

```html
<!DOCTYPE html>
<html lang="en">
<head>
<meta charset="utf-8">
<title>Velvet Ridge Chalet – Visit Card</title>
<link href="https://fonts.googleapis.com/css2?family=Oswald:wght@400;500&family=PT+Sans:wght@400;700&display=swap" rel="stylesheet">
<style>
  :root {
    --bg: #2a2a2b;
    --card-edge: #1b1616;
    --gold-light: #f6d97a;
    --gold-mid: #e9bd4c;
    --gold-deep: #c9952a;
    --ink: #1d1710;
    --wood-light: #e7c48a;
    --wood-mid: #b98346;
    --wood-dark: #6b4520;
    --wall: #efe3cf;
  }
  * { box-sizing: border-box; margin: 0; padding: 0; }
  html, body { width: 1200px; height: 890px; overflow: hidden; }
  body {
    background: var(--bg);
    position: relative;
    font-family: "PT Sans", sans-serif;
    color: var(--ink);
  }
  .card {
    position: absolute;
    left: 290px;
    width: 620px;
    height: 354px;
    background: var(--card-edge);
    padding: 9px;
  }
  .card--front { top: 70px; }
  .card--back { top: 466px; }
  .card__inner { position: relative; width: 100%; height: 100%; overflow: hidden; }

  /* Front */
  .interior-photo {
    position: absolute; inset: 0;
    background:
      linear-gradient(180deg, rgba(255,240,210,.35) 0%, rgba(0,0,0,0) 30%),
      linear-gradient(110deg, var(--wall) 0%, var(--wood-light) 25%, var(--wood-mid) 55%, var(--wood-light) 80%, var(--wood-mid) 100%);
  }
  .title-band {
    position: absolute; left: 0; right: 0; top: 118px; height: 92px;
    background: linear-gradient(90deg, rgba(233,189,76,.92), rgba(246,217,122,.95) 55%, rgba(233,189,76,.9));
  }
  .title-band__name {
    position: absolute; left: 150px; top: 20px;
    font-family: "Oswald", sans-serif; font-weight: 400;
    font-size: 34px; letter-spacing: .5px; text-transform: uppercase; line-height: 1;
  }
  .title-band__tagline {
    position: absolute; left: 152px; top: 62px;
    font-family: "Oswald", sans-serif; font-size: 9.5px; letter-spacing: 2.2px; text-transform: uppercase;
  }
  .title-band__social {
    position: absolute; right: 14px; top: 8px;
    display: flex; align-items: center; gap: 5px; font-size: 10px;
  }
  .social-dot { width: 9px; height: 9px; border-radius: 50%; border: 1.2px solid var(--ink); }

  /* Back */
  .info-panel {
    position: absolute; left: 0; top: 0; bottom: 0; width: 330px;
    background: linear-gradient(160deg, var(--gold-mid) 0%, var(--gold-light) 45%, var(--gold-mid) 100%);
    padding: 64px 22px 0 24px;
    font-size: 11px; line-height: 1.3;
  }
  .room-photo {
    position: absolute; left: 330px; top: 0; right: 0; bottom: 0;
    background:
      linear-gradient(180deg, var(--wall) 0%, var(--wall) 35%, rgba(0,0,0,0) 55%),
      linear-gradient(135deg, var(--wood-light) 0%, var(--wood-mid) 55%, var(--wood-dark) 100%);
  }
  .activities { display: flex; gap: 18px; margin: 10px 0 10px 6px; }
  .activities svg { width: 26px; height: 26px; }
  .channels { display: flex; gap: 16px; align-items: center; margin: 8px 0 16px; font-weight: 700; font-size: 14px; }
  .channels__item { display: flex; align-items: center; gap: 4px; }
  .channels__mark { width: 10px; height: 10px; border-radius: 50%; background: var(--ink); }
  .contact__title { font-weight: 700; font-size: 13px; margin-bottom: 4px; }
  .contact__row { font-size: 11px; line-height: 1.45; }
  .contact__row b { display: inline-block; width: 18px; }
</style>
</head>
<body>
  <section class="card card--front">
    <div class="card__inner">
      <div class="interior-photo" role="img" aria-label="Warm wooden chalet dining room with antler chandelier, stone fireplace and long table"></div>
      <div class="title-band">
        <div class="title-band__social"><span class="social-dot"></span>@velvetridgechalet</div>
        <h1 class="title-band__name">Velvet Ridge Chalet</h1>
        <p class="title-band__tagline">Luxury rental apartment in Hinterthal</p>
      </div>
    </div>
  </section>

  <section class="card card--back">
    <div class="card__inner">
      <div class="info-panel">
        <p>Hinterthal is a place where you will encounter freedom, adventure, culinary enjoyment, and pure happiness.</p>
        <div class="activities">
          <svg viewBox="0 0 26 26"><circle cx="13" cy="13" r="12" fill="none" stroke="currentColor" stroke-width="1.4"/><path d="M6 18 L11 10 L14 14 L16 12 L20 18 Z" fill="currentColor"/></svg>
          <svg viewBox="0 0 26 26"><circle cx="13" cy="13" r="12" fill="none" stroke="currentColor" stroke-width="1.4"/><path d="M13 6 V20 M7 9.5 L19 16.5 M19 9.5 L7 16.5" stroke="currentColor" stroke-width="1.6"/></svg>
          <svg viewBox="0 0 26 26"><circle cx="13" cy="13" r="12" fill="none" stroke="currentColor" stroke-width="1.4"/><circle cx="8.5" cy="15.5" r="3.2" fill="none" stroke="currentColor" stroke-width="1.4"/><circle cx="17.5" cy="15.5" r="3.2" fill="none" stroke="currentColor" stroke-width="1.4"/><path d="M8.5 15.5 L12 10 L17.5 15.5 M11 10 H14" fill="none" stroke="currentColor" stroke-width="1.3"/></svg>
          <svg viewBox="0 0 26 26"><circle cx="13" cy="13" r="12" fill="none" stroke="currentColor" stroke-width="1.4"/><path d="M11 6 V20" stroke="currentColor" stroke-width="1.5"/><path d="M11 6 L18 9 L11 12 Z" fill="currentColor"/></svg>
        </div>
        <p>Experience genuine exhilaration with Velvet Ridge Chalet and celebrate the luxury life in Hinterthal. Our apartment can be booked through</p>
        <div class="channels">
          <span class="channels__item">Staylane</span>
          <span class="channels__item"><span class="channels__mark"></span>Hearthly</span>
        </div>
        <div class="contact">
          <p class="contact__title">Contact us</p>
          <p class="contact__row"><b>T:</b>+420 604 918 352</p>
          <p class="contact__row"><b>E:</b>stay.brenvale@larkpost.net</p>
          <p class="contact__row"><b>W:</b>www.velvetridgechalet.com</p>
        </div>
      </div>
      <div class="room-photo" role="img" aria-label="Bright chalet living room with wooden table, antler chandelier and alpine flower painting"></div>
    </div>
  </section>
</body>
</html>
```